Brell Stone Company Business Cards

Front and Back Business Card - logo and text setup - cool design. I need workable photoshop or illustrator files so I can setup each employee card with design that is created
Updates

Hi everyone, thank you for the great entries. Please no more white and blue cards - there are so many already - black and silver only now please. thanks!

Target Market(s)

Construction Industry - Facility Managers

Industry/Entity Type

Construction

Contact Information for Business Card

I really like contemporary simplistic looks - clean neat....not opposed to seeing some black backrounds

Requirements
Must have
• Logo/website address with design on front only - www.brellstone-example.com (logo attached)
• Back:
• Name/Title/Company Address/Phone/email address
Nice to have
• Cool design
Should not have
• Nothing gimmicky like Fire or Water - since we are a Fire Protection company - it has all been done

```html
<!DOCTYPE html>
<html lang="en">
<head>
<meta charset="utf-8">
<title>Brell Stone Company Business Cards</title>
<link href="https://fonts.googleapis.com/css2?family=Work+Sans:wght@400;500;800&display=swap" rel="stylesheet">
<style>
  :root {
    --stage: #1c1c1c;
    --card-dark: #161616;
    --card-light: #ffffff;
    --black: #1b1b1b;
    --silver: #a9acb0;
    --silver-light: #c9cbce;
    --ink: #3a3a3a;
  }
  * { box-sizing: border-box; margin: 0; padding: 0; }
  html, body {
    width: 1200px; height: 900px; overflow: hidden;
    background: var(--stage);
    font-family: "Work Sans", Arial, sans-serif;
  }
  .stage { position: relative; width: 1200px; height: 900px; }
  .card {
    position: absolute; left: 290px; width: 620px; height: 354px;
    overflow: hidden;
    box-shadow: 0 18px 40px rgba(0,0,0,.55);
  }
  .card--front { top: 60px; background: var(--card-dark); }
  .card--back { top: 476px; background: var(--card-light); }

  .brand {
    display: flex; align-items: center; gap: 12px;
    font-weight: 800; letter-spacing: -0.5px;
  }
  .brand__mark { flex: none; }
  .card--front .brand {
    position: absolute; inset: 0;
    justify-content: center; font-size: 58px; color: var(--silver-light);
  }
  .card--front .brand__mark { width: 26px; height: 26px; background: var(--silver); }
  .card--back .brand {
    position: absolute; left: 34px; top: 30px; font-size: 40px; color: var(--black);
  }
  .card--back .brand__mark { width: 18px; height: 18px; background: var(--silver); }

  .person {
    position: absolute; right: 40px; top: 128px; text-align: right;
  }
  .person__name {
    font-size: 26px; font-weight: 500; color: var(--black);
    letter-spacing: 2px; text-transform: uppercase; line-height: 1;
  }
  .person__title {
    margin-top: 10px; font-size: 17px; line-height: 20px;
    color: var(--ink); letter-spacing: 1px;
  }
  .divider {
    position: absolute; left: 40px; right: 40px; top: 192px;
    height: 2px; background: var(--silver);
  }
  .contacts {
    position: absolute; left: 40px; top: 212px; list-style: none;
    font-size: 17px; color: var(--ink); letter-spacing: 0.8px;
  }
  .contacts li { display: flex; align-items: center; gap: 10px; line-height: 24px; }
  .contacts svg { width: 13px; height: 13px; flex: none; }
  .address {
    position: absolute; right: 40px; top: 246px; text-align: right;
    font-size: 17px; color: var(--ink); letter-spacing: 0.8px; line-height: 24px;
  }
  .band { position: absolute; left: 0; bottom: 0; width: 620px; height: 64px; }
</style>
</head>
<body>
<main class="stage">
  <section class="card card--front" aria-label="Card front">
    <div class="brand"><span class="brand__mark"></span>brell stone</div>
  </section>

  <section class="card card--back" aria-label="Card back">
    <div class="brand"><span class="brand__mark"></span>brell stone</div>

    <div class="person">
      <p class="person__name">Daniel Hart</p>
      <p class="person__title">Director</p>
    </div>
    <div class="divider"></div>

    <ul class="contacts">
      <li>
        <svg viewBox="0 0 16 16"><path fill="#1b1b1b" d="M4 1l3 3-2 2c1 2 3 4 5 5l2-2 3 3-2 3C7 15 1 9 1 3z"/></svg>
        (555) 014-2869
      </li>
      <li>
        <svg viewBox="0 0 16 16"><path fill="#1b1b1b" d="M4 1h8v4H4zM1 6h14v6h-3v3H4v-3H1zM5 10v4h6v-4z"/></svg>
        (555) 014-2866
      </li>
      <li>
        <svg viewBox="0 0 16 16"><rect x="1.5" y="3.5" width="13" height="9" fill="none" stroke="#1b1b1b" stroke-width="1.6"/><path d="M1.5 3.5L8 9l6.5-5.5" fill="none" stroke="#1b1b1b" stroke-width="1.6"/></svg>
        info@brellstone-example.com
      </li>
      <li>
        <svg viewBox="0 0 16 16"><g fill="none" stroke="#1b1b1b" stroke-width="1.3"><circle cx="8" cy="8" r="6.5"/><ellipse cx="8" cy="8" rx="3" ry="6.5"/><path d="M1.5 8h13M2.5 5h11M2.5 11h11"/></g></svg>
        www.brellstone-example.com
      </li>
    </ul>

    <p class="address">48 Meridian Park Way<br>Harlow Falls, NY 10990</p>

    <svg class="band" viewBox="0 0 620 64" aria-hidden="true">
      <path fill="var(--silver)" d="M0 26 L250 36 C262 37 268 40 272 44 L0 33 Z"/>
      <path fill="var(--black)" d="M0 40 L262 50 C290 50 300 36 340 36 L620 38 V64 H0 Z"/>
    </svg>
  </section>
</main>
</body>
</html>
```